Business Card Design

IT Solutions company.

I need a professional looking design with my company logo if possible.

Logo is located here:
http://www.brivelsystems.co.uk/dev/images/logo1.jpg
Feel free to redesign the logo if you think you have any better suggestions.

Our services include, IT Infrastructure/Telephony Maintenance & Hosting Services. Linux and Windows Solutions, App Development.

Out website is currently under development:
http://www.brivelsystems.co.uk/dev/

I'm looking for a colourful but professional looking business card.

Industry/Entity Type

Business

Contact Information for Business Card

Brivel Systems Group Ltd
Morven Halsey
07845193870
www.brivelsystems.co.uk
mhalsey@brivelsystems.co.uk

```html
<!DOCTYPE html>
<html lang="en">
<head>
<meta charset="utf-8">
<title>Brivel Systems Group Ltd — Business Card</title>
<link rel="stylesheet" href="https://fonts.googleapis.com/css2?family=Arimo:wght@400;700&display=swap">
<style>
  :root {
    --brand-blue: #1e3fa6;
    --brand-blue-deep: #162f86;
    --ink: #111111;
    --paper: #ffffff;
    --stage: #e9eaee;
  }
  * { margin: 0; padding: 0; box-sizing: border-box; }
  html, body { width: 1200px; height: 1000px; overflow: hidden; }
  body {
    background: var(--stage);
    font-family: "Arimo", Arial, sans-serif;
    color: var(--ink);
    position: relative;
  }
  .card {
    position: absolute;
    left: 220px;
    width: 760px;
    height: 434px;
    overflow: hidden;
    box-shadow: 0 6px 18px rgba(0,0,0,0.18);
  }
  .card--front { top: 40px; background: var(--paper); }
  .card--back { top: 526px; background: var(--brand-blue); }

  .front-bands { position: absolute; left: 0; bottom: 0; width: 760px; height: 90px; }

  .contact-block { position: absolute; left: 44px; top: 214px; font-size: 22px; line-height: 1.3; }
  .contact-block .company { font-size: 23px; letter-spacing: 0.3px; margin-bottom: 4px; }
  .contact-line { display: flex; align-items: center; gap: 12px; }
  .contact-line svg { flex: none; }

  .wordmark { display: flex; align-items: center; gap: 8px; font-weight: 700; color: var(--brand-blue); }
  .wordmark .dot { width: 26px; height: 26px; border: 3px solid var(--brand-blue); border-radius: 50%; }
  .card--front .wordmark { position: absolute; right: 44px; top: 150px; font-size: 22px; }

  .holder-name { position: absolute; right: 44px; top: 278px; font-size: 28px; }
  .holder-name b { font-weight: 700; }

  .back-band { position: absolute; left: 0; width: 100%; background: var(--paper); top: 262px; height: 84px; }
  .card--back .wordmark { position: absolute; left: 0; right: 0; top: 290px; justify-content: center; font-size: 24px; }
  .website { position: absolute; left: 0; right: 0; top: 366px; text-align: center; color: var(--paper); font-size: 26px; }
</style>
</head>
<body>
  <section class="card card--front" aria-label="Business card front">
    <div class="contact-block">
      <p class="company">BRIVEL SYSTEMS GROUP LTD</p>
      <p class="contact-line">
        <svg width="20" height="20" viewBox="0 0 20 20" aria-hidden="true"><rect width="20" height="20" rx="3" fill="var(--brand-blue)"/><path d="M6 4c-1 1-1.5 3 0 6s4 5.5 6.5 6c1 .2 2-.3 2.5-1l-2-2-1.5 1c-1.5-.8-3-2.5-3.6-4l1-1.3L7 4z" fill="#fff"/></svg>
        <span>078 4519 3870</span>
      </p>
      <p class="contact-line">
        <svg width="20" height="16" viewBox="0 0 20 16" aria-hidden="true"><rect width="20" height="16" fill="var(--brand-blue)"/><path d="M1 1l9 8 9-8" fill="none" stroke="#fff" stroke-width="1.6"/></svg>
        <span>mhalsey@brivelsystems.co.uk</span>
      </p>
    </div>

    <div class="wordmark"><span class="dot"></span><span>Brivel Systems</span></div>

    <p class="holder-name"><b>Morven</b> Halsey</p>

    <svg class="front-bands" viewBox="0 0 760 90" aria-hidden="true">
      <rect x="0" y="34" width="440" height="22" fill="var(--ink)"/>
      <path d="M0 56 H420 C440 56 440 30 470 28 H760 V90 H0 Z" fill="var(--brand-blue)"/>
    </svg>
  </section>

  <section class="card card--back" aria-label="Business card back">
    <div class="back-band"></div>
    <div class="wordmark"><span class="dot"></span><span>Brivel Systems</span></div>
    <p class="website">www.brivelsystems.co.uk</p>
  </section>
</body>
</html>
```